Business card for exciting VC company

Should look simple, crisp, and modern.

Industry/Entity Type

Venture Capital

Contact Information for Business Card

Would like to see at least one design that has our blue on the back with the tagline "Transforming Traditional Industry" and white front with contact details.

Font styles to use
Sans Serif

Requirements
Must have
• Logo

Gregory Tallis
gtallis@brindlewave.vc
Managing Partner
M (628)354-xxxx

```html
<!DOCTYPE html>
<html lang="en">
<head>
<meta charset="utf-8">
<title>Brindlewave Capital – Business Card</title>
<link rel="stylesheet" href="https://fonts.googleapis.com/css2?family=Lato:wght@400;700&display=swap">
<style>
  :root {
    --stage: #6e7070;
    --brand-blue: #3a77b7;
    --brand-blue-light: #4a86c3;
    --logo-light: #d3d6da;
    --ink: #1c1e22;
    --paper: #f7f7f6;
    --ghost: #ececeb;
    --tagline: #c8d4e3;
  }
  * { margin: 0; padding: 0; box-sizing: border-box; }
  html, body { width: 1200px; height: 866px; overflow: hidden; }
  body {
    background: var(--stage);
    font-family: "Lato", Arial, sans-serif;
    position: relative;
  }
  .card {
    position: absolute;
    top: 285px;
    width: 520px;
    height: 297px;
    overflow: hidden;
    box-shadow: 0 10px 24px rgba(0,0,0,0.35);
  }
  /* Back */
  .card-back { left: 55px; background: var(--brand-blue); }
  .world-map {
    position: absolute;
    left: 50px; top: 22px;
    width: 420px; height: 200px;
    background: radial-gradient(ellipse at center, var(--brand-blue-light) 0%, var(--brand-blue) 75%);
    border-radius: 40px;
  }
  .back-logo {
    position: absolute;
    left: 0; right: 0; top: 108px;
    text-align: center;
    color: var(--logo-light);
    font-weight: 700;
    font-size: 34px;
    letter-spacing: 3px;
  }
  .back-rule {
    position: absolute;
    left: 240px; top: 228px;
    width: 40px; height: 1px;
    background: var(--tagline);
  }
  .tagline {
    position: absolute;
    left: 0; right: 0; bottom: 30px;
    text-align: center;
    color: var(--tagline);
    font-size: 11px;
    letter-spacing: 3px;
    text-transform: uppercase;
  }
  /* Front */
  .card-front { left: 625px; background: var(--paper); }
  .ghost-name {
    position: absolute;
    color: var(--ghost);
    font-weight: 700;
    font-size: 96px;
    letter-spacing: 4px;
    line-height: 1;
    white-space: nowrap;
  }
  .ghost-first { right: -30px; top: -28px; }
  .ghost-last { right: -10px; bottom: -34px; }
  .front-logo {
    position: absolute;
    left: 34px; top: 130px;
    color: var(--ink);
    font-weight: 700;
    font-size: 24px;
    letter-spacing: 1.5px;
  }
  .contact {
    position: absolute;
    left: 300px; top: 86px;
    color: var(--ink);
  }
  .contact-name { color: var(--brand-blue); font-weight: 700; font-size: 18px; }
  .contact-title { font-size: 14px; margin-top: 6px; }
  .contact-rule { width: 18px; height: 2px; background: var(--brand-blue); margin: 16px 0 14px; }
  .contact-line { font-size: 14px; line-height: 1.5; }
</style>
</head>
<body>
  <section class="card card-back" aria-label="Card back">
    <div class="world-map" role="img" aria-label="Faint dotted world map"></div>
    <div class="back-logo">Brindlewave Capital</div>
    <div class="back-rule"></div>
    <p class="tagline">Transforming Traditional Industry</p>
  </section>

  <section class="card card-front" aria-label="Card front">
    <span class="ghost-name ghost-first" aria-hidden="true">GREGORY</span>
    <span class="ghost-name ghost-last" aria-hidden="true">TALLIS</span>
    <div class="front-logo">Brindlewave Capital</div>
    <div class="contact">
      <p class="contact-name">Gregory Tallis</p>
      <p class="contact-title">Managing Partner</p>
      <div class="contact-rule"></div>
      <p class="contact-line">gtallis@brindlewave.vc</p>
      <p class="contact-line">(628)354-xxxx</p>
    </div>
  </section>
</body>
</html>
```